WP website design (Brisko)

We need a wordpress design that will incorporate a professional color scheme with company logo in a clean layout. The design needs to consider that this will be developed on a responsive theme. Colors are that of the logo and and an accent color (perhaps light brown/tan). Client wants a 'modern' look.

Industry/Entity Type

It Company

Font styles to use
Serif
Sans Serif

Colors

Designer to choose colors to be used in the design.

Requirements
Must have
• Must Have:
- Navigation: 1) Home 2) Real Estate Listings 3) Auctions 4) Buyers 5) Sellers 6) Services 7) Meet the Crew 8) Contact Us

Site will have a slideshow element (image attached) and the following widgets: 1) Featured Auctions 2) Testimonials blog widget 3) 'Auction Alerts' email sign up 4) FB Posts RSS.

In the footer, there will be smaller company logo, the affiliations logo, and contact info below:
Brisko Auctions & Realty, Inc.
58391 Corvan Hollow Road • Suite 604 • Orlando, FL 32899
Office: 407.555.0148 / Cell: 407.555.0193 / Fax: 407.555.0176
Email: info@briskoauctions.example
Nice to have
• - - Site will have drop-down menus - please indicate the styling, for instance the dropdown menus 1) Upcoming Auctions 2) Past Auctions under the 'Auctions' link

```html
<!DOCTYPE html>
<html lang="en">
<head>
<meta charset="utf-8">
<title>Brisko Auctions &amp; Realty</title>
<link href="https://fonts.googleapis.com/css2?family=Source+Sans+3:wght@400;600;700&family=Roboto:ital,wght@0,400;0,500;0,700;1,400&display=swap" rel="stylesheet">
<style>
:root{
  --tan:#e8b18c;
  --red:#a5232f;
  --red-dark:#8c1b26;
  --black:#111;
  --cream:#fdf2ea;
  --panel:#efefef;
  --line:#c9c9c9;
  --text:#222;
  --link:#d8102a;
}
*{box-sizing:border-box;margin:0;padding:0}
html,body{width:948px;height:1200px;overflow:hidden}
body{background:var(--tan);font-family:"Roboto",Arial,sans-serif;color:var(--text);position:relative}
.page{position:absolute;left:78px;top:0;width:792px;height:1200px;background:#fff}
.abs{position:absolute}

/* navigation */
.main-nav{position:absolute;left:0;top:0;width:792px;height:38px;background:var(--red);display:flex;z-index:3}
.main-nav a{display:flex;align-items:center;justify-content:center;color:#fff;text-decoration:none;font:600 13px "Source Sans 3",sans-serif;letter-spacing:.2px;border-right:1px solid rgba(255,255,255,.18);height:38px}
.main-nav a:last-child{border-right:none}
.main-nav a.active{background:var(--black)}
.dropdown{position:absolute;left:227px;top:38px;width:135px;z-index:4;border-bottom:5px solid var(--red)}
.dropdown a{display:block;height:29px;line-height:29px;padding-left:12px;color:#fff;font:400 13px "Source Sans 3",sans-serif;letter-spacing:.3px;text-decoration:none;background:var(--red)}
.dropdown a.current{background:var(--black);border-top:1px solid #555}

/* header */
.hero{position:absolute;left:0;top:38px;width:792px;height:232px;background:linear-gradient(90deg,#fdf1ea 0%,#fbece3 32%,#d7d8d4 52%,#a9b0a6 75%,#8f9a8b 100%)}
.hero-logo{position:absolute;left:22px;top:62px;color:var(--red);font:600 52px/1 "Source Sans 3",sans-serif;letter-spacing:1px}
.hero-logo span{display:block;font-size:19px;letter-spacing:15px;margin-top:10px;padding-left:28px}

/* intro */
.intro{left:24px;top:300px;width:460px;font:600 14.5px/27px "Source Sans 3",sans-serif;letter-spacing:.2px;color:#1b1b1b}

/* listings */
.listing{position:absolute;left:25px;width:485px;height:246px;background:var(--cream);border:1px solid #b9b2ad}
.listing-head{height:36px;background:linear-gradient(#3a3a3a,#050505);border-radius:6px 6px 0 0;margin:-1px -1px 0;color:#fff;font:700 14.5px/36px "Roboto",sans-serif;padding-left:17px;letter-spacing:.3px}
.thumb{position:absolute;left:28px;top:45px;width:126px;height:84px;background:linear-gradient(135deg,#6f8a5c,#b8bdb8 45%,#d7d7d2 60%,#55703f);box-shadow:3px 3px 3px rgba(0,0,0,.35)}
.btn{position:absolute;left:56px;width:83px;height:28px;background:var(--red);border-radius:4px;color:#fff;font:400 11px/28px "Roboto",sans-serif;box-shadow:0 1px 2px rgba(0,0,0,.3)}
.btn svg{position:absolute;left:9px;top:7px}
.btn span{position:absolute;left:32px}
.listing h3{position:absolute;left:177px;top:54px;font:700 13.5px "Source Sans 3",sans-serif;letter-spacing:1px}
.listing .desc{position:absolute;left:177px;top:77px;width:260px;font:400 11.3px/14.5px "Roboto",sans-serif}
.listing .bill{position:absolute;left:261px;top:112px;color:var(--link);font:700 12.3px "Roboto",sans-serif}
.listing .info{position:absolute;left:178px;top:139px;width:270px;font:400 11.3px/15.4px "Roboto",sans-serif;letter-spacing:.3px}
.info b{font-weight:500}
.info .loc{position:relative;padding-left:14px}
.info .loc svg{position:absolute;left:0;top:3px}
.info .date{padding-left:51px}

.partner-badge{left:211px;top:961px;width:152px;height:48px;border:1px solid #ccc;border-radius:5px;background:linear-gradient(#fff,#f0f3f6)}
.partner-badge i{position:absolute;left:10px;top:12px;width:110px;height:22px;background:#dbe3ec;border-radius:11px}

/* sidebar */
.widget{position:absolute;left:548px;width:230px;border:1px solid #bdbdbd;background:var(--panel)}
.widget-head{height:39px;background:var(--red);color:#fff;font:400 21px/40px "Source Sans 3",sans-serif;padding-left:19px;letter-spacing:.3px;margin:-1px -1px 0}
.alerts{left:547px;top:305px;width:231px;height:125px;background:var(--red);border:none;border-radius:3px;color:#fff;box-shadow:0 1px 3px rgba(0,0,0,.35)}
.alerts h2{position:absolute;left:15px;top:8px;font:400 24px "Source Sans 3",sans-serif;letter-spacing:.3px}
.alerts .ring{position:absolute;right:10px;top:14px;width:56px;height:56px;border:6px solid rgba(255,255,255,.12);border-radius:50%}
.alerts p{position:absolute;left:15px;top:45px;width:190px;font:400 10.4px/14px "Roboto",sans-serif}
.alerts .signup{position:absolute;left:15px;top:82px;width:106px;height:30px;background:#f6d9c3;border:1px solid #5a1a1a;border-radius:5px;color:#1a1a1a;font:600 14px/28px "Source Sans 3",sans-serif;text-align:center;box-shadow:1px 2px 2px rgba(0,0,0,.35)}
.featured{top:457px;height:247px}
.featured .name{position:absolute;top:52px;left:0;width:100%;text-align:center;font:500 9.8px/14.5px "Roboto",sans-serif}
.featured .photo{position:absolute;left:48px;top:90px;width:141px;height:86px;border:2px solid #333;background:linear-gradient(135deg,#6f8a5c,#b8bdb8 45%,#d7d7d2 60%,#55703f)}
.featured .lot{position:absolute;top:194px;left:0;width:100%;text-align:center;font:400 10.2px/12.3px "Roboto",sans-serif}
.testimonials{top:733px;height:192px}
.quote-mark{position:absolute;left:12px;top:43px;font:700 32px/1 Georgia,serif;color:#b0b0b0}
.quote{position:absolute;left:19px;top:57px;width:200px;font:italic 400 10.4px/15.6px "Roboto",sans-serif;text-indent:22px}
.author{position:absolute;left:17px;top:164px;color:var(--red);font:italic 400 10.4px "Roboto",sans-serif}
.social{top:952px;height:121px}
.social-row{position:absolute;top:58px;left:33px;display:flex;gap:23px}
.social-row span{width:39px;height:39px;border-radius:2px;color:#fff;font:600 10px/39px "Source Sans 3",sans-serif;text-align:center}
.s1{background:#3a5a98}.s2{background:#3fb4e8}.s3{background:#e6662b}

/* footer */
.site-footer{position:absolute;left:0;top:1100px;width:792px;height:100px;background:var(--red)}
.contact{position:absolute;left:16px;top:15px;color:#fff;font:400 10.6px/17.6px "Roboto",sans-serif}
.contact strong{font-weight:700}
.foot-logo{position:absolute;left:334px;top:20px;color:#fff;font:600 30px/1 "Source Sans 3",sans-serif;text-align:center}
.foot-logo span{display:block;font-size:11px;letter-spacing:8px;margin-top:8px;padding-left:4px}
.badges{position:absolute;left:555px;top:17px;display:flex;gap:14px;align-items:center}
.badges i{display:block;background:rgba(255,255,255,.85)}
.copy{position:absolute;right:17px;top:64px;color:#fff;text-align:right;font:400 8.4px/17.6px "Roboto",sans-serif}
</style>
</head>
<body>
<div class="page">
  <nav class="main-nav">
    <a style="width:75px">Home</a>
    <a style="width:152px">Real Estate Listings</a>
    <a class="active" style="width:91px">Auctions</a>
    <a style="width:79px">Buyers</a>
    <a style="width:79px">Sellers</a>
    <a style="width:89px">Services</a>
    <a style="width:124px">Meet the Crew</a>
    <a style="width:103px">Contact Us</a>
  </nav>
  <div class="dropdown">
    <a>Upcoming auctions</a>
    <a class="current">Past auctions</a>
  </div>

  <header class="hero" role="img" aria-label="Slideshow photo of a white stucco house with arched entry and palm trees">
    <div class="hero-logo">Brisko<span>AUCTIONS</span></div>
  </header>

  <p class="abs intro">Brisko Auctions &amp; Realty, Inc. is the only call needed for all of your assets evaluation and disposition needs.</p>

  <article class="listing" style="top:373px">
    <div class="listing-head">372 HARLOW MEDICAL DR</div>
    <div class="thumb" role="img" aria-label="Photo of the listed property"></div>
    <div class="btn" style="top:148px"><svg width="14" height="14" viewBox="0 0 14 14"><rect x="1" y="3" width="8" height="10" fill="#fff"/><rect x="5" y="1" width="8" height="10" fill="#cfe0f0" stroke="#fff"/></svg><span>Details</span></div>
    <div class="btn" style="top:183px"><svg width="15" height="14" viewBox="0 0 15 14"><rect x="0.5" y="2" width="14" height="11" fill="#f5d77a" stroke="#fff"/><rect x="3" y="5" width="9" height="6" fill="#5aa05a"/></svg><span>Photos</span></div>
    <h3>FT COMMERCIAL BUILDING</h3>
    <p class="desc">Selling 3120 Acres of land in tracts of 2590 Acres &amp; 560 Acres</p>
    <p class="bill">Click here to view Sale Bill!</p>
    <div class="info">
      <div>LIVE OFF-SITE AUCTION</div>
      <div><b>Auction Location:</b></div>
      <div class="loc"><svg width="9" height="12" viewBox="0 0 9 12"><path d="M4.5 0C2 0 0 2 0 4.4 0 7.5 4.5 12 4.5 12S9 7.5 9 4.4C9 2 7 0 4.5 0z" fill="#d21a1a"/></svg>418 N Carrow Ave, Melvale, OK 73901</div>
      <div><b>Property Location:</b></div>
      <div class="loc"><svg width="9" height="12" viewBox="0 0 9 12"><path d="M4.5 0C2 0 0 2 0 4.4 0 7.5 4.5 12 4.5 12S9 7.5 9 4.4C9 2 7 0 4.5 0z" fill="#d21a1a"/></svg>418 N Carrow Ave, Melvale, OK 73901</div>
      <div class="date">08/21/14 at 10:00 AM CDT</div>
    </div>
  </article>

  <article class="listing" style="top:664px;left:27px">
    <div class="listing-head">372 HARLOW MEDICAL DR</div>
    <div class="thumb" role="img" aria-label="Photo of the listed property"></div>
    <div class="btn" style="top:148px"><svg width="14" height="14" viewBox="0 0 14 14"><rect x="1" y="3" width="8" height="10" fill="#fff"/><rect x="5" y="1" width="8" height="10" fill="#cfe0f0" stroke="#fff"/></svg><span>Details</span></div>
    <div class="btn" style="top:183px"><svg width="15" height="14" viewBox="0 0 15 14"><rect x="0.5" y="2" width="14" height="11" fill="#f5d77a" stroke="#fff"/><rect x="3" y="5" width="9" height="6" fill="#5aa05a"/></svg><span>Photos</span></div>
    <h3>FT COMMERCIAL BUILDING</h3>
    <p class="desc">Selling 3120 Acres of land in tracts of 2590 Acres &amp; 560 Acres</p>
    <p class="bill">Click here to view Sale Bill!</p>
    <div class="info">
      <div>LIVE OFF-SITE AUCTION</div>
      <div><b>Auction Location:</b></div>
      <div class="loc"><svg width="9" height="12" viewBox="0 0 9 12"><path d="M4.5 0C2 0 0 2 0 4.4 0 7.5 4.5 12 4.5 12S9 7.5 9 4.4C9 2 7 0 4.5 0z" fill="#d21a1a"/></svg>418 N Carrow Ave, Melvale, OK 73901</div>
      <div><b>Property Location:</b></div>
      <div class="loc"><svg width="9" height="12" viewBox="0 0 9 12"><path d="M4.5 0C2 0 0 2 0 4.4 0 7.5 4.5 12 4.5 12S9 7.5 9 4.4C9 2 7 0 4.5 0z" fill="#d21a1a"/></svg>418 N Carrow Ave, Melvale, OK 73901</div>
      <div class="date">08/21/14 at 10:00 AM CDT</div>
    </div>
  </article>

  <div class="abs partner-badge" role="img" aria-label="Partner badge"><i></i></div>

  <aside>
    <section class="widget alerts">
      <div class="ring"></div>
      <h2>Auction Alerts</h2>
      <p>Please join our free mailing list to get auction alerts.</p>
      <div class="signup">Sign Up Now</div>
    </section>

    <section class="widget featured">
      <div class="widget-head">Featured Auctions</div>
      <p class="name">13.35 ACRES OF PRIME DEVELOP<br>&amp; 33RD STREET</p>
      <div class="photo" role="img" aria-label="Photo of the featured property"></div>
      <p class="lot">LOTS 13 &amp; 14 FOR SALE, PELLFORD<br>IOWA<br>Third Street, Pellford, IA 52690</p>
    </section>

    <section class="widget testimonials">
      <div class="widget-head">Testimonials Blog</div>
      <div class="quote-mark">&ldquo;</div>
      <p class="quote">It is a long established fact that a reader will be distracted by the readable content of a page when looking at its layout. The point of using Lorem Ipsum is that it has a more-or-less normal distribution of letters...</p>
      <p class="author">Dorian Welles...</p>
    </section>

    <section class="widget social">
      <div class="widget-head">Social Media</div>
      <div class="social-row">
        <span class="s1">Follow</span>
        <span class="s2">Posts</span>
        <span class="s3">Feed</span>
      </div>
    </section>
  </aside>

  <footer class="site-footer">
    <div class="contact">
      <strong>Brisko Auctions &amp; Realty, Inc.</strong><br>
      58391 Corvan Hollow Road • Suite 604 • Orlando, FL 32899<br>
      Office: 407.555.0148 / Cell: 407.555.0193 / Fax: 407.555.0176<br>
      Email: info@briskoauctions.example
    </div>
    <div class="foot-logo">Brisko<span>AUCTIONS</span></div>
    <div class="badges" role="img" aria-label="Affiliation badges">
      <i style="width:56px;height:34px;border-radius:50%"></i>
      <i style="width:32px;height:34px"></i>
      <i style="width:66px;height:22px"></i>
      <i style="width:26px;height:30px"></i>
    </div>
    <p class="copy">Copyright © 2014 • Brisko Auctions, Inc. • All Rights Reserved<br>Powered by: BidHarbor.example &amp; Kindle Labs</p>
  </footer>
</div>
</body>
</html>
```